Technology Enablement - One Pager

I need (2) one pager piece of marketing collateral to use as outreach for a service offering. The one pager must have a strong call to action, highlight the pain points the service solves.

```html
<!DOCTYPE html>
<html lang="en">
<head>
<meta charset="utf-8">
<title>Technology Enablement – One Pagers</title>
<link href="https://fonts.googleapis.com/css2?family=Roboto:wght@300;400;500;700;900&display=swap" rel="stylesheet">
<style>
:root{
  --backdrop:#6e6e6e;
  --blue:#1590cf;
  --blue-deep:#1b6fa8;
  --blue-light:#6cb9e4;
  --panel-top:#2c8fca;
  --panel-bottom:#4b5e86;
  --dark:#232025;
  --slate:#4a5878;
  --slate-text:#3a4866;
  --ink:#1e1e22;
  --white:#ffffff;
  --mist:#e6ebf1;
}
*{margin:0;padding:0;box-sizing:border-box}
html,body{width:1200px;height:872px;overflow:hidden}
body{background:var(--backdrop);font-family:"Roboto",Arial,sans-serif;position:relative}
.sheet{position:absolute;top:84px;width:942px;height:1332px;transform:scale(0.53);transform-origin:0 0;overflow:hidden;background:var(--white);color:var(--white);box-shadow:0 20px 40px rgba(0,0,0,.45)}
.sheet--smb{left:86px}
.sheet--trades{left:615px}
.sheet svg.backdrop{position:absolute;left:0;top:0}
.block{position:absolute}
h2,h3{font-weight:700}
p,li{font-size:16.5px;line-height:20px;font-weight:400}
ul{padding-left:23px}
.brand{position:absolute;left:44px;top:38px;font-size:70px;font-weight:700;color:var(--blue);letter-spacing:-1px}
.hero-title{position:absolute;font-weight:900;color:var(--white);line-height:0.95;letter-spacing:0.5px}
.hero-rule{position:absolute;height:3px;background:var(--white)}
.hero-lede{position:absolute;font-size:22px;line-height:27px;font-weight:300;color:var(--white)}
.side-head{font-size:26px;margin-bottom:6px}
.divider{position:absolute;height:1.5px;background:rgba(255,255,255,.8)}
.tag-box{position:absolute;height:37px;padding:3px 12px;font-size:26px;font-weight:500;color:var(--ink)}
.tag-box--fade{background:linear-gradient(90deg,#f2f7fb 0%,#cfe3f2 40%,var(--blue) 100%)}
.tag-box--slate{background:var(--slate);color:var(--white);font-weight:700}
.tag-box--plain{background:var(--white);color:var(--slate-text);font-weight:700}
.assess-title{font-size:34px;line-height:40px;font-weight:700}
.assess-rule{position:absolute;height:3px;background:linear-gradient(90deg,#9aa3ad,rgba(154,163,173,0))}
.price{font-size:26px;font-weight:700;margin:6px 0 8px}
.footer-band{position:absolute;left:0;width:942px;height:28px;text-align:center;font-size:18px;line-height:28px;color:var(--white);font-weight:500}
.footer-cta{position:absolute;left:0;width:942px;text-align:center;color:var(--ink)}
.trades li{line-height:24.5px}
.dark-text{color:var(--ink)}
</style>
</head>
<body>

<!-- SMB one pager -->
<section class="sheet sheet--smb">
  <svg class="backdrop" width="942" height="1332" viewBox="0 0 942 1332">
    <defs>
      <linearGradient id="smbSide" x1="0" y1="0" x2="0" y2="1">
        <stop offset="0" stop-color="#2c8fca"/>
        <stop offset="1" stop-color="#4b5e86"/>
      </linearGradient>
      <linearGradient id="smbPhoto" x1="0" y1="0" x2="1" y2="1">
        <stop offset="0" stop-color="#6fb7dd"/>
        <stop offset="0.5" stop-color="#2a8cc6"/>
        <stop offset="1" stop-color="#1a74b4"/>
      </linearGradient>
      <linearGradient id="smbHex" x1="0" y1="0" x2="1" y2="1">
        <stop offset="0" stop-color="#3b5670"/>
        <stop offset="0.6" stop-color="#1a3550"/>
        <stop offset="1" stop-color="#0e2238"/>
      </linearGradient>
    </defs>
    <rect x="0" y="265" width="470" height="980" fill="url(#smbSide)"/>
    <polygon points="0,265 540,0 942,0 942,280 470,280" fill="url(#smbPhoto)" role="img" aria-label="Photo of a smiling team of office professionals"/>
    <rect x="470" y="280" width="472" height="965" fill="var(--dark)"/>
    <polygon points="185,24 345,24 420,157 345,290 185,290 110,157" fill="url(#smbHex)" stroke="#233548" stroke-width="4" role="img" aria-label="Photo of a hand touching a rising digital bar chart"/>
    <line x1="390" y1="220" x2="470" y2="280" stroke="#ffffff" stroke-width="2"/>
  </svg>

  <div class="brand">Norvanta</div>
  <h1 class="hero-title" style="left:472px;top:46px;font-size:42px">TECHNOLOGY<br>ENABLEMENT – SMB</h1>
  <div class="hero-rule" style="left:472px;top:132px;width:440px"></div>
  <p class="hero-lede" style="left:505px;top:146px;width:420px">Your technology shouldn’t slow your business down.</p>
  <p class="hero-lede" style="left:505px;top:210px;width:420px">We help SMBs turn disconnected tools into systems that actually work.</p>

  <!-- left column -->
  <div class="block" style="left:42px;top:302px;width:415px">
    <h2 class="side-head">The Problem</h2>
    <p>Most growing businesses have plenty of software — but no real system.<br>You’ve invested in cloud tools, CRMs, accounting platforms, HR apps, and automation.<br>Yet day-to-day work still feels harder than it should.</p>
  </div>
  <div class="divider" style="left:42px;top:449px;width:370px"></div>
  <div class="block" style="left:42px;top:456px;width:415px">
    <h2 class="side-head">Common Pain Points</h2>
    <ul>
      <li>Software doesn’t talk to each other</li>
      <li>Key processes live in people’s heads</li>
      <li>Manual work fills the gaps between systems</li>
      <li>Decisions are made without clear data</li>
      <li>Tech choices are made reactively, not strategically</li>
    </ul>
  </div>
  <div class="divider" style="left:42px;top:622px;width:370px"></div>
  <div class="block" style="left:42px;top:630px;width:415px">
    <h2 class="side-head">The Result?</h2>
    <p>More effort, more admin, and less return on your software spend.</p>
  </div>
  <div class="divider" style="left:42px;top:713px;width:370px"></div>
  <div class="block" style="left:42px;top:720px;width:420px">
    <h2 class="side-head">What We Do</h2>
    <p>Technology Enablement is about improving how work actually flows through your business.<br>Norvanta helps you:</p>
    <ul style="margin-top:4px">
      <li>Identify workflow and process gaps</li>
      <li>Find where technology is creating friction (not value)</li>
      <li>Improve adoption of the tools you already pay for</li>
      <li>Clarify where automation and integration will actually help</li>
      <li>Build a practical roadmap tied to real business outcomes</li>
    </ul>
    <p style="font-size:19px;font-weight:500;margin-top:6px">This is not IT support.</p>
    <p>It’s operational improvement, using technology as the lever.</p>
  </div>
  <div class="tag-box tag-box--fade" style="left:42px;top:1061px;width:358px;padding-left:24px">Our Approach Is Different</div>
  <div class="block" style="left:42px;top:1110px;width:420px">
    <ul>
      <li>You do not need to switch IT providers</li>
      <li>You do not need to rip and replace systems</li>
      <li>You do not need a long-term contract</li>
    </ul>
    <p style="margin-top:10px">We start with clarity first.<br>Execution comes later — only where it makes sense.</p>
  </div>

  <!-- right column -->
  <div class="block" style="left:495px;top:310px;width:420px">
    <h2 class="assess-title"><span style="color:var(--blue-light)">Technology Enablement</span><br>Assessment</h2>
  </div>
  <div class="assess-rule" style="left:495px;top:400px;width:325px"></div>
  <div class="block" style="left:495px;top:422px;width:420px">
    <p style="font-size:19px;font-weight:700;line-height:24px">A 2–4-week, stand-alone engagement</p>
    <p style="font-size:19px;font-weight:500;line-height:24px;margin:8px 0 6px">We assess your:</p>
    <ul>
      <li>Technology &amp; digital maturity</li>
      <li>Core workflows and handoffs</li>
      <li>Integration and automation opportunities</li>
      <li>Adoption gaps and training needs</li>
      <li>Data, reporting, and KPI visibility</li>
      <li>IT and security posture (at a business level)</li>
    </ul>
  </div>
  <div class="tag-box tag-box--fade" style="left:495px;top:634px;width:357px">You Receive:</div>
  <div class="block" style="left:495px;top:678px;width:420px">
    <p>A prioritized 5–10 item Improvement Roadmap, each with:</p>
    <ul>
      <li>Business impact</li>
      <li>Relative effort</li>
      <li>ROI potential</li>
    </ul>
    <p class="price">Price: $2,500</p>
    <p>No upsell required. No obligation beyond the assessment.</p>
  </div>
  <div class="tag-box tag-box--fade" style="left:495px;top:876px;width:357px">Who This Is For</div>
  <div class="block" style="left:495px;top:918px;width:420px">
    <ul>
      <li>Small and mid-sized businesses</li>
      <li>Leadership teams feeling “tech pressure” but lacking a plan</li>
      <li>Companies scaling headcount faster than systems</li>
      <li>Owners tired of guessing which tools to buy next</li>
    </ul>
  </div>
  <div class="tag-box tag-box--fade" style="left:495px;top:1060px;width:357px">Why Start Here</div>
  <div class="block" style="left:495px;top:1100px;width:420px">
    <p>Because buying more software without fixing workflows just adds complexity.</p>
    <p style="margin-top:10px">This assessment gives you:</p>
    <ul>
      <li>Clarity instead of opinions</li>
      <li>A roadmap instead of random fixes</li>
      <li>Confidence before spending more money</li>
    </ul>
  </div>

  <div class="footer-band" style="top:1245px;background:var(--blue)">Start with insight. Move forward with confidence.</div>
  <div class="footer-cta" style="top:1278px;font-size:17px;font-weight:500;line-height:21px">Let’s identify what’s actually holding your business back — and how to fix it.<br><span style="color:var(--slate);font-weight:700">Book a Technology Enablement Assessment</span></div>
</section>

<!-- Trades one pager -->
<section class="sheet sheet--trades trades">
  <svg class="backdrop" width="942" height="1332" viewBox="0 0 942 1332">
    <defs>
      <linearGradient id="tradesPhoto" x1="0" y1="0" x2="1" y2="0">
        <stop offset="0" stop-color="#5a6a8c"/>
        <stop offset="0.6" stop-color="#4a5b80"/>
        <stop offset="1" stop-color="#1d2c45"/>
      </linearGradient>
      <linearGradient id="tradesLeft" x1="0" y1="0" x2="0" y2="1">
        <stop offset="0" stop-color="#d8dde4"/>
        <stop offset="0.08" stop-color="#ffffff"/>
      </linearGradient>
      <linearGradient id="tradesBlue" x1="0" y1="0" x2="0" y2="1">
        <stop offset="0" stop-color="#1c8ccb"/>
        <stop offset="1" stop-color="#1592d2"/>
      </linearGradient>
    </defs>
    <rect x="0" y="222" width="470" height="1023" fill="url(#tradesLeft)"/>
    <rect x="470" y="222" width="472" height="1023" fill="url(#tradesBlue)"/>
    <polygon points="0,0 942,0 942,272 820,222 0,222" fill="url(#tradesPhoto)" role="img" aria-label="Photo of a team reviewing data on a large screen in a dim office"/>
    <polygon points="0,165 690,165 825,222 0,222" fill="#201d22"/>
  </svg>

  <h1 class="hero-title" style="left:42px;top:46px;font-size:46px;line-height:40px">TECHNOLOGY ENABLEMENT<br>FOR TRADES</h1>
  <p class="block" style="left:42px;top:128px;font-size:22px;font-weight:700;color:var(--white)">Electrical, Plumbing, HVAC, Mechanical, Construction</p>
  <p class="block" style="left:42px;top:170px;font-size:19px;line-height:24px;font-weight:700;color:var(--white)">Your jobs are physical. Your problems aren’t.<br>We help trade businesses fix the tech and workflows behind the work.</p>

  <!-- left column -->
  <div class="block dark-text" style="left:42px;top:266px;width:430px">
    <h2 style="font-size:32px;color:var(--blue);margin-bottom:4px">The Reality in the Trades</h2>
    <p>Trade companies rely on technology more than ever — even if they don’t call it “IT.”<br>Scheduling. Estimating. Job tracking. Invoicing. Payroll. Field apps.<br>Most of it works… kind of.</p>
    <p style="font-weight:500;margin:8px 0 2px">Common frustrations:</p>
    <ul>
      <li>Office and field systems don’t line up</li>
      <li>Dispatch process is manual or inefficient.</li>
      <li>Jobs get quoted one way and invoiced another</li>
      <li>Information is stuck in texts, notebooks, or someone’s phone</li>
      <li>Admin work grows faster than revenue</li>
      <li>Technology decisions fall to “whoever knows computers”</li>
    </ul>
    <p style="font-weight:500;margin-top:2px;width:400px">The work gets done — but it takes more effort than it should.</p>
  </div>
  <div class="tag-box tag-box--slate" style="left:42px;top:695px;width:418px">What We Do</div>
  <div class="block dark-text" style="left:42px;top:743px;width:420px">
    <p>We help trade companies simplify operations using technology they already depend on.<br>Norvanta focuses on:</p>
    <ul>
      <li>How work flows from quote → job → invoice → reporting</li>
      <li>How office and field tools connect (or don’t)</li>
      <li>Where manual steps create delays, rework, or missed revenue</li>
      <li>Why tools aren’t being fully used by crews or admin staff</li>
    </ul>
    <p>This is about making the business easier to run — not selling IT jargon.</p>
  </div>
  <div class="tag-box tag-box--slate" style="left:42px;top:1039px;width:418px">Why Trades Like Our Approach</div>
  <div class="block dark-text" style="left:42px;top:1082px;width:420px">
    <ul>
      <li>Low-risk, practical, and clear</li>
      <li>No pressure to replace systems</li>
      <li>No requirement to change IT providers</li>
      <li>Focused on productivity, not tech for tech’s sake</li>
    </ul>
    <p style="margin-top:6px">We earn trust by fixing real problems first.</p>
  </div>

  <!-- right column -->
  <div class="block" style="left:495px;top:264px;width:430px">
    <h2 class="assess-title" style="font-size:34px">Technology Enablement<br>Assessment</h2>
  </div>
  <div class="assess-rule" style="left:495px;top:354px;width:325px;background:linear-gradient(90deg,#4ab0e6,rgba(74,176,230,0))"></div>
  <p class="block" style="left:495px;top:376px;width:430px;font-size:20px;line-height:25px;font-weight:700">A 2–4 week, stand-alone assessment built specifically for trades</p>
  <div class="tag-box tag-box--plain" style="left:495px;top:455px;width:417px">We review:</div>
  <div class="block" style="left:495px;top:502px;width:420px">
    <ul style="list-style:disc">
      <li style="line-height:20px">Job management workflows</li>
      <li style="line-height:20px">Quoting → scheduling → invoicing flow</li>
      <li style="line-height:20px">Field tools and adoption gaps</li>
      <li style="line-height:20px">Office vs field handoffs</li>
      <li style="line-height:20px">Reporting visibility (jobs, labour, margins)</li>
      <li style="line-height:20px">Security and data risks (without fear tactics)</li>
    </ul>
  </div>
  <div class="tag-box tag-box--plain" style="left:495px;top:640px;width:417px">You Receive:</div>
  <div class="block" style="left:495px;top:681px;width:430px">
    <p>A Trades-Specific Improvement Roadmap showing:</p>
    <ul>
      <li style="line-height:20px">Where time and money are being lost</li>
      <li style="line-height:20px">What to fix first</li>
      <li style="line-height:20px">What can wait</li>
      <li style="line-height:20px">Where automation or integration actually pays off</li>
    </ul>
    <p class="price" style="margin:8px 0 2px">Price: $2,500</p>
    <p>Straightforward. No obligation beyond the assessment.</p>
  </div>
  <div class="tag-box tag-box--plain" style="left:495px;top:873px;width:417px">Who This Is For</div>
  <div class="block" style="left:495px;top:920px;width:425px">
    <ul>
      <li style="line-height:20px">Electrical, plumbing, HVAC, mechanical, GC, and construction firms</li>
      <li style="line-height:20px">Owners feeling buried in admin</li>
      <li style="line-height:20px">Companies growing past “winging it”</li>
      <li style="line-height:20px">Trades relying on multiple apps that don’t work well together</li>
    </ul>
  </div>
  <div class="tag-box tag-box--plain" style="left:495px;top:1055px;width:417px">Why Start With an Assessment</div>
  <div class="block" style="left:495px;top:1104px;width:425px">
    <p>Because guessing costs more than clarity.<br>This gives you:</p>
    <ul>
      <li style="line-height:20px">A clear plan instead of piecemeal fixes</li>
      <li style="line-height:20px">Confidence before spending on new tools</li>
      <li style="line-height:20px">A roadmap aligned to how trades actually work</li>
    </ul>
  </div>

  <div class="footer-band" style="top:1245px;background:var(--slate)">Fix the systems behind the scenes — so the work runs smoother on site.</div>
  <div class="footer-cta" style="top:1279px;font-size:23px;font-weight:500">Book a Trades Technology Enablement Assessment</div>
</section>

</body>
</html>
```